business card with logo

Would like a business card for an electrical contractor called BRANLOCK ELECTRICS.
No generic electrical imagery (light globe, powerpoints, ect). Would like a logo or symbol created in the design as part of the project . I would like crisp colour. No templated designs like Printvox

is there any other designers willing to submit designs

Electrical

```html
<!DOCTYPE html>
<html lang="en">
<head>
<meta charset="utf-8">
<title>Branlock Electrics – Business Card</title>
<link href="https://fonts.googleapis.com/css2?family=Michroma&family=Open+Sans:wght@400;600&display=swap" rel="stylesheet">
<style>
  :root {
    --bg: #e6e6e6;
    --card-white: #ffffff;
    --brand-blue: #0a8ad0;
    --brand-blue-deep: #0a5f9c;
    --brand-orange: #f5821f;
    --brand-red: #8e1a1f;
    --ink-blue: #1d3f73;
    --ink-dark: #3a2a1a;
  }
  * { margin: 0; padding: 0; box-sizing: border-box; }
  html, body { width: 1200px; height: 900px; overflow: hidden; }
  body {
    background: var(--bg);
    display: flex;
    flex-direction: column;
    align-items: center;
    justify-content: center;
    gap: 40px;
    font-family: "Open Sans", sans-serif;
  }
  .card {
    width: 660px;
    height: 377px;
    background: var(--card-white);
    box-shadow: 0 6px 18px rgba(0,0,0,0.15);
    position: relative;
    overflow: hidden;
  }

  /* Front */
  .card-front { padding: 14px; }
  .front-panel {
    width: 100%; height: 100%;
    background: radial-gradient(ellipse at 60% 35%, var(--brand-blue) 0%, var(--brand-blue-deep) 100%);
    display: flex; flex-direction: column; align-items: center; justify-content: center;
    gap: 26px;
  }
  .brand-mark {
    width: 78px; height: 78px; border-radius: 50%;
    background: var(--brand-orange);
  }
  .brand-name {
    font-family: "Michroma", sans-serif;
    font-size: 30px;
    letter-spacing: 1px;
    color: var(--card-white);
    white-space: nowrap;
  }

  /* Back */
  .card-back { padding-top: 40px; }
  .back-header {
    display: flex; align-items: center; gap: 14px;
    padding-left: 40px;
  }
  .back-header .brand-mark { width: 56px; height: 56px; }
  .back-header .brand-name { color: var(--brand-red); font-size: 23px; }
  .holder-name {
    text-align: center;
    margin-top: 28px;
    color: var(--ink-blue);
    font-weight: 600;
    font-size: 17px;
  }
  .band-orange {
    margin: 4px 24px 0;
    height: 30px;
    background: var(--brand-orange);
    display: flex; align-items: center; justify-content: center;
    color: var(--ink-dark);
    font-size: 15px;
  }
  .band-blue {
    margin: 0 24px;
    height: 52px;
    background: var(--brand-blue);
    display: flex; align-items: center; justify-content: center; gap: 8px;
    color: var(--card-white);
    font-size: 15px;
  }
  .band-blue-lower {
    margin: 12px 24px 0;
    height: 48px;
    background: var(--brand-blue);
  }
</style>
</head>
<body>
  <section class="card card-back">
    <div class="back-header">
      <span class="brand-mark"></span>
      <span class="brand-name">BRANLOCK ELECTRICS</span>
    </div>
    <p class="holder-name">Liam Harker</p>
    <div class="band-orange">Rec#40318</div>
    <div class="band-blue">
      <svg class="icon-mail" width="18" height="13" viewBox="0 0 18 13" aria-hidden="true">
        <rect x="0.75" y="0.75" width="16.5" height="11.5" rx="1.5" fill="none" stroke="#ffffff" stroke-width="1.5"/>
        <path d="M1 1.5 L9 7.5 L17 1.5" fill="none" stroke="#ffffff" stroke-width="1.5"/>
      </svg>
      <span>branlockelec@postmail.com</span>
    </div>
    <div class="band-blue-lower"></div>
  </section>

  <section class="card card-front">
    <div class="front-panel">
      <span class="brand-mark"></span>
      <span class="brand-name">BRANLOCK ELECTRICS</span>
    </div>
  </section>
</body>
</html>
```